Project Calm Harbor; Retail packaging for handmade bar soap.

A clean design that conveys quality and affordable luxury. Wrapper material is 80 lb felt cover paper, used as a wrap around the product.

Attached is my idea. Logo is purchased. Unless you think it's terrible, maybe best is to refine what I have? I'm thinking fonts, proportions, etc. Honestly though, if you think it's bad we can start from scratch. I think it's good but I'm not that invested in it. I just want to sell good soap.
5 different fragrances, each identical packaging except the colored stripe and the scent name. Should the scent name be inside the colored stripe or above it?

Apologies for the non-metric:
Soap is 3" tall and 2-13/16" wide and 1" deep.
Front of label is 2-5/16" tall and 2-13/16" wide.
Label (wrap) is 8-1/2" long

Looking forward to hearing from you guys.

Target Market(s)

retail gift shops, health food stores, hotel gift shops.

Industry/Entity Type

retail and online personal care products

Other font styles liked:
• not decorative or script

Colors
0054AA
0677BA
7BADD7
CADEEF
E8F1F8
59FF00
82FF00
B8FF75
E3FFCB
F4FFEA
FFF300
FFF600
FEFA6F
FFFEC7
FFFEE8
EB3D1F
EC4F4E
F09395
F8D3D4
FCEDEE
A7469A
B969AE
D3A5CF
EDDBEB
F8F0F9

Requirements
Must have
• The best word I can think of is feng shui. My soap makes you feel good when you use it. It's simple and clean. I want the same in the label.

```html
<!DOCTYPE html>
<html lang="en">
<head>
<meta charset="utf-8">
<title>Calm Harbor Soap Co. – Coconut and Lemongrass Wrap</title>
<link href="https://fonts.googleapis.com/css2?family=Rubik:wght@400;500&family=Rokkitt:wght@400&display=swap" rel="stylesheet">
<style>
  :root {
    --backdrop: #b7b7b2;
    --paper: #ffffff;
    --ink: #1c1c1c;
    --ink-soft: #3a3a3a;
    --wash-strong: #e9eda0;
    --wash-soft: #fffec7;
    --shadow: rgba(0, 0, 0, 0.22);
  }
  * { margin: 0; padding: 0; box-sizing: border-box; }
  html, body {
    width: 1200px;
    height: 900px;
    overflow: hidden;
    background: var(--backdrop);
  }
  .wrap-label {
    position: absolute;
    left: 40px;
    top: 297px;
    width: 1120px;
    height: 305px;
    background: var(--paper);
    box-shadow: 0 3px 8px var(--shadow);
    color: var(--ink);
    font-family: "Rubik", sans-serif;
  }

  /* Back panel */
  .feature-icons {
    position: absolute;
    left: 8px;
    top: 92px;
    width: 52px;
    text-align: center;
  }
  .feature {
    height: 58px;
  }
  .feature svg {
    display: block;
    margin: 0 auto 2px;
  }
  .feature-name {
    font-size: 5px;
    letter-spacing: 0.3px;
    line-height: 6px;
    text-transform: uppercase;
    color: var(--ink-soft);
  }
  .back-panel {
    position: absolute;
    left: 146px;
    top: 52px;
    width: 300px;
    text-align: center;
  }
  .ingredients-title {
    font-size: 13px;
    font-weight: 500;
    letter-spacing: 0.3px;
    margin-bottom: 3px;
  }
  .ingredients-list {
    font-size: 9.8px;
    line-height: 13.4px;
    letter-spacing: 0.2px;
  }
  .web-address {
    margin-top: 40px;
    font-size: 12px;
    font-weight: 500;
    letter-spacing: 0.3px;
  }
  .slogan {
    margin-top: 46px;
    font-size: 8px;
    line-height: 13px;
    letter-spacing: 1.8px;
    text-transform: uppercase;
  }

  /* Spine */
  .spine-scent {
    position: absolute;
    left: 552px;
    top: 106px;
    width: 30px;
    height: 120px;
    writing-mode: vertical-rl;
    font-size: 9.5px;
    line-height: 13px;
    letter-spacing: 3.2px;
    text-transform: uppercase;
  }

  /* Front panel */
  .front-panel {
    position: absolute;
    left: 713px;
    top: 0;
    width: 240px;
    height: 305px;
    text-align: center;
  }
  .color-wash {
    position: absolute;
    left: 70px;
    top: 120px;
    width: 120px;
    height: 170px;
    border-radius: 48% 52% 40% 60% / 40% 45% 55% 60%;
    background: radial-gradient(ellipse at 55% 40%, var(--wash-strong) 0%, var(--wash-soft) 55%, rgba(255, 254, 232, 0) 78%);
  }
  .brand-name {
    position: absolute;
    left: 0;
    top: 33px;
    width: 240px;
    font-size: 13.5px;
    line-height: 16px;
    letter-spacing: 2.6px;
    text-transform: uppercase;
  }
  .brand-mark {
    position: absolute;
    left: 106px;
    top: 106px;
    width: 28px;
    height: 28px;
    border: 1px solid var(--ink);
    border-radius: 50%;
  }
  .tagline {
    position: absolute;
    left: 0;
    top: 184px;
    width: 240px;
    font-family: "Rokkitt", serif;
    font-size: 8.5px;
    line-height: 12px;
    letter-spacing: 2px;
    text-transform: uppercase;
  }
  .scent-name {
    position: absolute;
    left: 0;
    top: 224px;
    width: 240px;
    font-size: 14px;
    font-weight: 500;
    line-height: 16px;
    letter-spacing: 4.5px;
    text-transform: uppercase;
  }
  .net-weight {
    position: absolute;
    top: 283px;
    font-family: "Rokkitt", serif;
    font-size: 14px;
    letter-spacing: 0.5px;
  }
  .net-weight.metric { left: 720px; }
  .net-weight.imperial { left: 996px; }
</style>
</head>
<body>
  <main class="wrap-label">

    <ul class="feature-icons" style="list-style:none">
      <li class="feature">
        <svg width="24" height="26" viewBox="0 0 24 26" fill="none" stroke="#1c1c1c" stroke-width="1.1" stroke-linecap="round">
          <path d="M5 14 C4 9 6 6 8 8 L9 12"/>
          <path d="M9 12 L8 4 C8 2 10.5 2 10.5 4 L11 11"/>
          <path d="M11 11 L11.5 3 C11.5 1 14 1 14 3 L13.5 11"/>
          <path d="M13.5 11 L15 5 C15.5 3 18 3.5 17.5 5.5 L16 13"/>
          <path d="M16 13 C18 12 20 13 19 15 C17 19 14 23 9 22 C6 21 5 18 5 14"/>
          <path d="M9 17 C10 15 12 15 13 17 C12 19 10 19 9 17 Z"/>
        </svg>
        <div class="feature-name">Handmade</div>
      </li>
      <li class="feature">
        <svg width="26" height="24" viewBox="0 0 26 24" fill="none" stroke="#1c1c1c" stroke-width="1.1" stroke-linecap="round">
          <path d="M3 12 H23 C23 18 19 21 13 21 C7 21 3 18 3 12 Z"/>
          <path d="M9 21 V23 H17 V21"/>
          <path d="M8 12 C8 8 11 6 14 6 C16 6 18 7 19 9"/>
          <path d="M12 12 C12 9 13 8 15 8"/>
          <path d="M14 6 L16 2 M16 2 C18 2 19 3 19 5"/>
        </svg>
        <div class="feature-name">All natural<br>ingredients</div>
      </li>
      <li class="feature">
        <svg width="26" height="26" viewBox="0 0 26 26" fill="none" stroke="#1c1c1c" stroke-width="1.1" stroke-linecap="round">
          <rect x="3" y="15" width="20" height="8" rx="2"/>
          <path d="M6 15 C6 12 9 11 13 11 C17 11 20 12 20 15"/>
          <circle cx="11" cy="7" r="2"/>
          <circle cx="16" cy="4" r="1.4"/>
          <circle cx="14" cy="9" r="1"/>
          <path d="M6 19 H20"/>
        </svg>
        <div class="feature-name">Variety of<br>soap scents</div>
      </li>
    </ul>

    <section class="back-panel">
      <h2 class="ingredients-title">Ingredients:</h2>
      <p class="ingredients-list">
        Saponified Oils: (Coconut, Olive, Sustainable Certified Palm,<br>
        Cocoa Butter and Castor oil)<br>
        Goodies: glycerin, artesian spring water, white porcelain clay,<br>
        Oregon honey, fermentation derived natural citric acid and<br>
        lactic acid, Oregon sea salt, natural fragrances and natural<br>
        earth colorants
      </p>
      <p class="web-address">CalmHarbor.us</p>
      <p class="slogan">Buy good coffee?<br>Buy good soap!</p>
    </section>

    <p class="spine-scent">Coconut and<br>Lemongrass</p>

    <section class="front-panel">
      <div class="color-wash" role="img" aria-label="Soft pale yellow watercolor wash in the scent colour"></div>
      <h1 class="brand-name">Calm Harbor<br>Soap Co.</h1>
      <span class="brand-mark" aria-hidden="true"></span>
      <p class="tagline">All-natural and handmade<br>on the coast</p>
      <p class="scent-name">Coconut and<br>Lemongrass</p>
    </section>

    <span class="net-weight metric">115gr</span>
    <span class="net-weight imperial">4oz</span>
  </main>
</body>
</html>
```